Signage for a store*

logo on the two sides of the sign
in the middle is the name of the store witch is VORELT
at the bottom of the two logos, one side for location/address and the other side is contact details phone number is 718-392-6107 address is 2974 THE SIGN WILL BEE 15 FEET BY 4 FEET I WOULD LIKE THAT THE
BACKGROUND OF THE SIGN SHOULD HAVE A NICE COLOR BASE
THAT GOES FOR A WINE STORE

```html
<!DOCTYPE html>
<html lang="en">
<head>
<meta charset="utf-8">
<title>VORELT – Store Signage</title>
<link href="https://fonts.googleapis.com/css2?family=Courier+Prime:wght@400;700&family=Roboto:wght@700&display=swap" rel="stylesheet">
<style>
  :root {
    --wine: #a02645;
    --cream: #f2ebd8;
    --gold: #c9a24a;
    --board: #b4b5b5;
    --pattern: #ad3553;
  }
  * { box-sizing: border-box; margin: 0; padding: 0; }
  html, body { width: 1200px; height: 1200px; overflow: hidden; }
  body {
    background: var(--board);
    position: relative;
    font-family: "Roboto", Arial, sans-serif;
  }
  .sign {
    position: absolute;
    left: 145px;
    width: 869px;
    height: 232px;
    display: flex;
    flex-direction: column;
  }
  .sign--one { top: 176px; }
  .sign--two { top: 468px; }
  .sign--three { top: 769px; }

  .sign__main {
    position: relative;
    height: 191px;
    display: flex;
    align-items: center;
    justify-content: space-between;
    padding: 0 28px;
    overflow: hidden;
  }
  .sign__pattern {
    position: absolute;
    inset: 0;
    background: radial-gradient(ellipse at 50% 50%, var(--pattern), var(--wine) 75%);
  }
  .sign__strip {
    height: 41px;
    display: flex;
    align-items: center;
    justify-content: space-between;
    padding: 0 16px 0 20px;
    font-weight: 700;
    font-size: 31px;
    letter-spacing: 0.5px;
  }
  .contact { display: flex; align-items: center; gap: 8px; }
  .contact svg { width: 22px; height: 26px; }

  .logo {
    position: relative;
    width: 124px;
    height: 160px;
    display: flex;
    flex-direction: column;
    align-items: center;
    justify-content: center;
    gap: 12px;
  }
  .logo__dot {
    width: 46px;
    height: 46px;
    border-radius: 50%;
  }
  .logo__name {
    font-family: "Courier Prime", "Courier New", monospace;
    font-size: 25px;
    font-weight: 400;
    letter-spacing: 0.5px;
  }
  .store-name {
    position: relative;
    font-family: "Courier Prime", "Courier New", monospace;
    font-weight: 700;
    font-size: 122px;
    letter-spacing: 6px;
    line-height: 1;
  }

  /* light sign */
  .sign--light .sign__main { background: var(--cream); color: var(--wine); }
  .sign--light .sign__strip { background: var(--wine); color: var(--cream); }
  .sign--light .logo__dot { background: var(--gold); }
  .sign--light .contact svg { fill: var(--cream); stroke: var(--cream); }

  /* dark sign */
  .sign--dark .sign__main { background: var(--wine); color: var(--cream); }
  .sign--dark .sign__strip { background: var(--cream); color: var(--wine); }
  .sign--dark .logo__dot { background: var(--cream); }
  .sign--dark .contact svg { fill: var(--wine); stroke: var(--wine); }
</style>
</head>
<body>

<section class="sign sign--one sign--light">
  <div class="sign__main">
    <div class="logo"><span class="logo__dot"></span><span class="logo__name">VORELT</span></div>
    <h1 class="store-name">VORELT</h1>
    <div class="logo"><span class="logo__dot"></span><span class="logo__name">VORELT</span></div>
  </div>
  <div class="sign__strip">
    <span class="contact">
      <svg viewBox="0 0 22 26"><path stroke="none" d="M11 0a10 10 0 0 0-10 10c0 7 10 16 10 16s10-9 10-16A10 10 0 0 0 11 0zm0 14a4 4 0 1 1 0-8 4 4 0 0 1 0 8z"/></svg>
      2974
    </span>
    <span class="contact">
      <svg viewBox="0 0 26 26"><path stroke="none" d="M6 2l4 5-2 3c1 3 4 6 7 7l3-2 5 4-3 4C12 23 3 14 2 5z"/><path fill="none" stroke-width="2" d="M14 6a6 6 0 0 1 6 6M14 1a11 11 0 0 1 11 11"/></svg>
      718 392 6107
    </span>
  </div>
</section>

<section class="sign sign--two sign--dark">
  <div class="sign__main">
    <div class="logo"><span class="logo__dot"></span><span class="logo__name">VORELT</span></div>
    <h1 class="store-name">VORELT</h1>
    <div class="logo"><span class="logo__dot"></span><span class="logo__name">VORELT</span></div>
  </div>
  <div class="sign__strip">
    <span class="contact">
      <svg viewBox="0 0 22 26"><path stroke="none" d="M11 0a10 10 0 0 0-10 10c0 7 10 16 10 16s10-9 10-16A10 10 0 0 0 11 0zm0 14a4 4 0 1 1 0-8 4 4 0 0 1 0 8z"/></svg>
      2974
    </span>
    <span class="contact">
      <svg viewBox="0 0 26 26"><path stroke="none" d="M6 2l4 5-2 3c1 3 4 6 7 7l3-2 5 4-3 4C12 23 3 14 2 5z"/><path fill="none" stroke-width="2" d="M14 6a6 6 0 0 1 6 6M14 1a11 11 0 0 1 11 11"/></svg>
      718 392 6107
    </span>
  </div>
</section>

<section class="sign sign--three sign--dark">
  <div class="sign__main">
    <div class="sign__pattern" role="img" aria-label="Faint wine-toned pattern of vine leaves, grapes and scattered letters"></div>
    <div class="logo"><span class="logo__dot"></span><span class="logo__name">VORELT</span></div>
    <h1 class="store-name">VORELT</h1>
    <div class="logo"><span class="logo__dot"></span><span class="logo__name">VORELT</span></div>
  </div>
  <div class="sign__strip">
    <span class="contact">
      <svg viewBox="0 0 22 26"><path stroke="none" d="M11 0a10 10 0 0 0-10 10c0 7 10 16 10 16s10-9 10-16A10 10 0 0 0 11 0zm0 14a4 4 0 1 1 0-8 4 4 0 0 1 0 8z"/></svg>
      2974
    </span>
    <span class="contact">
      <svg viewBox="0 0 26 26"><path stroke="none" d="M6 2l4 5-2 3c1 3 4 6 7 7l3-2 5 4-3 4C12 23 3 14 2 5z"/><path fill="none" stroke-width="2" d="M14 6a6 6 0 0 1 6 6M14 1a11 11 0 0 1 11 11"/></svg>
      718 392 6107
    </span>
  </div>
</section>

</body>
</html>
```